Velvet corsaro

I want a business card design. the company is an infrastructure development company.

Target Market(s)

Government
real estate investors
real estate clients

Industry/Entity Type

Business

```html
<!DOCTYPE html>
<html lang="en">
<head>
<meta charset="UTF-8">
<title>Velvet corsaro — Business Card</title>
<link rel="stylesheet" href="https://fonts.googleapis.com/css2?family=Lato:wght@400;700&display=swap">
<style>
  :root {
    --backdrop: #dcdcdc;
    --card-white: #ffffff;
    --brand-red: #e8333d;
    --brand-blue: #2fa9e0;
    --ink-light: #ffffff;
  }
  * { margin: 0; padding: 0; box-sizing: border-box; }
  html, body {
    width: 1200px;
    height: 750px;
    overflow: hidden;
    background: var(--backdrop);
  }
  .canvas {
    width: 1200px;
    height: 750px;
    display: flex;
    align-items: center;
    justify-content: center;
  }
  .business-card {
    width: 960px;
    height: 540px;
    display: block;
    font-family: "Lato", sans-serif;
  }
  .band-white { fill: var(--card-white); }
  .band-red { fill: var(--brand-red); }
  .band-blue { fill: var(--brand-blue); }
  .brand-name { fill: var(--brand-red); font-weight: 700; font-size: 26px; letter-spacing: 1px; }
  .brand-mark { fill: var(--brand-blue); }
  .holder-name { fill: var(--ink-light); font-size: 24px; }
  .holder-detail { fill: var(--ink-light); font-size: 22px; }
  .office-detail { fill: var(--ink-light); font-size: 13px; }
  .office-divider { stroke: var(--brand-red); stroke-width: 3; }
  .sector-tag { fill: var(--ink-light); font-size: 12px; }
</style>
</head>
<body>
<main class="canvas">
  <svg class="business-card" viewBox="0 0 960 540" xmlns="http://www.w3.org/2000/svg" aria-label="Velvet corsaro business card">
    <defs>
      <clipPath id="card-shape">
        <rect x="0" y="0" width="960" height="540" rx="44" ry="44"/>
      </clipPath>
    </defs>
    <g clip-path="url(#card-shape)">
      <rect class="band-white" x="0" y="0" width="960" height="540"/>
      <polygon class="band-red" points="0,235 960,88 960,125 0,335"/>
      <polygon class="band-blue" points="0,335 960,125 960,540 0,540"/>
    </g>

    <g class="brand-lockup">
      <rect class="brand-mark" x="662" y="34" width="30" height="30"/>
      <text class="brand-name" x="702" y="59">VELVET CORSARO</text>
    </g>

    <g class="office-block">
      <line class="office-divider" x1="612" y1="215" x2="612" y2="300"/>
      <text class="office-detail" x="626" y="228">12 Harbour Lane, Off Crest Link Road,</text>
      <text class="office-detail" x="626" y="248">Eastgate District, Coastland</text>
      <text class="office-detail" x="626" y="268">+234 8010045218, +234 7052281936</text>
      <text class="office-detail" x="626" y="288">info@velvetcorsaro.com www.velvetcorsaro.com</text>
      <text class="sector-tag" x="800" y="330">Infrastructure Development</text>
    </g>

    <g class="holder-block">
      <text class="holder-name" x="230" y="400">Tolani Marsh</text>
      <text class="holder-detail" x="230" y="428">MD.</text>
      <text class="holder-detail" x="230" y="456">+234 8010045218, +234 7052281936</text>
      <text class="holder-detail" x="230" y="484">tolani@velvetcorsaro.com</text>
    </g>
  </svg>
</main>
</body>
</html>
```